Pool Builder Website Design in arizona

Our current site is located here: tidemoor.net

We are looking to give this a modern facelift. We will be cutting your design into a wordpress theme so we can utilize the CMS plateform backend.

Look and Feel
• Clean cut and professional
• Mobile friendly
• Updated from old site
• Feel intrigued but relax (do you have trust logos? Odile looking into this)
Colors
• Warm tropical neutral colors
• Orange, brown, blues
- Please make the site modern and more sleek look that looks like a 2015 style design and NOT 1999.
- Must be coded as a wordpress theme
- must create a home page, inner page and blog page
- must allow client to BLOG using the post section in wordpress

This pool company is a pool builder/installer in Phoenix arizona.

NOTE::: Please create a home page and one internal page.

Industry/Entity Type

Builder

Coding

Coded - Design and coding required

Number of Pages Required

3 page

Font styles to use
Serif
Sans Serif

Requirements
Must have
• - Must be coded as a wordpress theme
• - must create a home page, inner page and blog page
• - must allow client to BLOG using the post section in wordpress

```html
<!DOCTYPE html>
<html lang="en">
<head>
<meta charset="utf-8">
<title>Tidemoor Pools – The Fiberglass Pool Experts</title>
<link href="https://fonts.googleapis.com/css2?family=Cinzel+Decorative:wght@700&family=Open+Sans:ital,wght@0,300;0,400;0,600;1,400&display=swap" rel="stylesheet">
<style>
:root{
  --sky-top:#a9cdf6;
  --sky-bottom:#cfe3fb;
  --nav:#3f6fc4;
  --nav-dark:#3563b5;
  --nav-line:#5683cf;
  --panel:#ffffff;
  --heading-blue:#3a6ec0;
  --heading-green:#7bb839;
  --text:#7a7f86;
  --link:#4d7fc8;
  --chevron:#7bb839;
  --rule:#e4e8ee;
  --footer-text:#6f9ad6;
}
*{margin:0;padding:0;box-sizing:border-box}
html,body{width:726px;height:1200px;overflow:hidden}
body{
  position:relative;
  background:linear-gradient(180deg,var(--sky-top) 0%,var(--sky-bottom) 30%,var(--sky-bottom) 100%);
  font-family:"Open Sans",Arial,sans-serif;
  color:var(--text);
}
.abs{position:absolute}

.coast-scene{left:0;top:136px;width:726px;height:196px;
  background:linear-gradient(180deg,#c5def8 0%,#3a8fdc 25%,#2a78cc 55%,#e9f3fd 85%,var(--sky-bottom) 100%)}

.brand{left:58px;top:22px;display:flex;align-items:center;gap:7px;
  font-weight:600;font-size:17px;color:var(--heading-blue)}
.brand-dot{width:14px;height:14px;border-radius:50%;background:var(--heading-green)}

.search{left:488px;top:29px;width:173px;height:25px;background:#fdfdfb;
  border:1px solid #e3e6ea;display:flex;align-items:center;justify-content:space-between;padding:0 8px;
  font-size:9px;color:#8a8f96}

.main-nav{left:54px;top:85px;width:620px;height:34px;background:linear-gradient(180deg,var(--nav),var(--nav-dark));display:flex}
.main-nav a{display:flex;align-items:center;justify-content:center;color:#fff;font-size:8px;letter-spacing:.3px;text-decoration:none;border-right:1px solid var(--nav-line)}
.main-nav a:last-child{border-right:none}

.panel{left:54px;top:119px;width:620px;height:972px;background:var(--panel);box-shadow:0 0 4px rgba(60,100,160,.15)}

.hero{left:66px;top:125px;width:595px;height:269px;
  background:linear-gradient(180deg,#2f7fd8 0%,#7ab8ec 30%,#a4572d 48%,#e9dfc9 56%,#3cb5e6 70%,#1e8fd0 100%)}
.hero-shadow{left:80px;top:394px;width:567px;height:12px;border-radius:50%;
  background:radial-gradient(ellipse at top,rgba(0,0,0,.25),rgba(0,0,0,0) 70%)}
.hero-title{left:81px;top:300px;font-family:"Cinzel Decorative",Georgia,serif;font-weight:700;font-size:27px;color:#fff;letter-spacing:.3px}
.hero-tag{left:81px;top:337px;font-weight:300;font-size:15px;color:#fff}
.hero-dots{left:81px;top:376px;display:flex;gap:2px}
.hero-dots span{width:9px;height:9px;border-radius:50%;border:1.5px solid #3a7ccc;background:transparent}
.hero-dots span.active{border-color:var(--heading-green)}

.section-title{font-family:"Cinzel Decorative",Georgia,serif;font-weight:700;font-size:14.8px;color:var(--heading-blue)}
.section-title .accent{color:var(--heading-green)}
.body-text{font-size:5.9px;line-height:12.2px;color:var(--text)}

.welcome-title{left:66px;top:430px}
.welcome-text{left:66px;top:457px;width:356px}

.options{left:66px;top:502px;display:flex}
.option-col{height:78px}
.option-col h3{font-weight:400;font-size:8.5px;color:var(--link);margin-bottom:4px}
.option-col li{list-style:none;font-style:italic;font-size:6.2px;line-height:12px;color:var(--text)}
.option-col li::before{content:"»";color:var(--chevron);font-style:normal;font-weight:600;margin-right:5px}
.col-brands{width:62px;border-right:1px solid var(--rule)}
.col-sizes{width:66px;margin-left:28px;border-right:1px solid var(--rule)}
.col-styles{width:67px;margin-left:31px;border-right:1px solid var(--rule)}
.col-colors{width:80px;margin-left:24px}

.feature-photo{left:446px;top:433px;width:214px;height:145px;border:2px solid #fff;outline:1px solid var(--rule);
  background:linear-gradient(180deg,#4f8fd6 0%,#8cc2ee 25%,#2f9de0 40%,#1a6fc2 100%)}
.slide-arrow{top:495px;width:14px;height:22px;background:rgba(255,255,255,.6);display:flex;align-items:center;justify-content:center}

.rule{left:66px;width:595px;height:1px;background:var(--rule)}

.portfolio-title{left:0;width:726px;top:617px;text-align:center}
.portfolio-text{left:110px;width:506px;top:642px;text-align:center}

.tile{width:143px;height:104px;border:2px solid #fff;outline:1px solid #e3e6ea}
.tile-feature{background:linear-gradient(160deg,#2f5e9e,#5a8cc6);padding:10px 8px;color:#fff}
.tile-feature h4{font-weight:600;font-size:10px;letter-spacing:.3px;margin-bottom:8px}
.tile-feature p{font-style:italic;font-size:6.2px;line-height:11.5px;color:#dbe7f6}
.tile-icons{position:absolute;right:8px;bottom:7px;display:flex;gap:4px}
.p1{background:linear-gradient(180deg,#3d7a4a 0%,#c9d7e2 30%,#2e9de0 55%,#1c6fc4 100%)}
.p2{background:linear-gradient(180deg,#1a1d26 0%,#333a48 35%,#1e4f9a 70%,#c58a7a 100%)}
.p3{background:linear-gradient(180deg,#a98a6e 0%,#6a5a48 35%,#2b5fa6 65%,#b59276 100%)}
.p4{background:linear-gradient(180deg,#8ec2ec 0%,#4b7a3e 30%,#3fc4f0 60%,#8a7a66 100%)}
.p5{background:linear-gradient(180deg,#2e74d2 0%,#a4572d 40%,#2fb5e8 65%,#1f8fd0 100%)}
.p6{background:linear-gradient(180deg,#4f8fd6 0%,#90c6ee 30%,#2f9de0 50%,#1a6fc2 100%)}
.p7{background:linear-gradient(180deg,#3c86dc 0%,#a7d2f2 40%,#4fc8ee 65%,#e8eef2 100%)}

.about-title{left:0;width:726px;top:933px;text-align:center}
.about-text{left:106px;width:514px;top:961px;text-align:center}

.cta{left:302px;top:1028px;width:123px;height:27px;background:var(--nav);border:1px solid #2f5aa6;
  color:#fff;font-size:8px;display:flex;align-items:center;justify-content:center}

.social{left:311px;top:1116px;display:flex;gap:9px}
.social span{width:20px;height:20px;border-radius:50%;border:1px solid #9dbde6;background:#fff}

.footer-nav{left:0;width:726px;top:1153px;text-align:center;font-size:6.6px;color:var(--footer-text)}
.footer-nav .sep{margin:0 8px}
.copyright{left:0;width:726px;top:1176px;text-align:center;font-size:6.4px;color:var(--footer-text)}
</style>
</head>
<body>

<div class="abs coast-scene" role="img" aria-label="Beach scenery with ocean, palm trees and splashing water behind the page"></div>

<div class="abs brand"><span class="brand-dot"></span>Tidemoor Pools</div>

<div class="abs search">
  <span>Search</span>
  <svg width="8" height="8" viewBox="0 0 10 10"><circle cx="4" cy="4" r="3" fill="none" stroke="#555" stroke-width="1.3"/><line x1="6.3" y1="6.3" x2="9" y2="9" stroke="#555" stroke-width="1.3"/></svg>
</div>

<div class="abs panel"></div>

<nav class="abs main-nav">
  <a style="width:102px">HOME</a>
  <a style="width:84px">STYLE</a>
  <a style="width:106px">PORTFOLIO</a>
  <a style="width:118px">INSTALLATION</a>
  <a style="width:102px">ABOUT &nbsp;US</a>
  <a style="width:108px">CONTACT US</a>
</nav>

<div class="abs hero" role="img" aria-label="Resort pool with blue loungers and white umbrellas on a wooden deck"></div>
<div class="abs hero-shadow"></div>
<div class="abs hero-title">TIDEMOOR POOLS</div>
<div class="abs hero-tag">The Fiberglass Pool Experts!</div>
<div class="abs hero-dots"><span></span><span class="active"></span><span></span><span></span></div>

<h2 class="abs section-title welcome-title"><span class="accent">WELCOME TO</span> TIDEMOOR POOLS</h2>
<p class="abs body-text welcome-text">At Tidemoor Pools, customizing your fiberglass pool is simple. We carry all the top brands, and can customize them to create the perfect poool for your little slice of paradise. With many shapes, sizes, styles and options to choose from, meet your needs and match your yard. Below is a list of different options for you to customize.</p>

<div class="abs options">
  <div class="option-col col-brands"><h3>Brands</h3><ul><li>Nordstar</li><li>Costa Linda</li><li>Lanai</li><li>Nordstar</li><li>Costa Linda</li></ul></div>
  <div class="option-col col-sizes"><h3>Sizes</h3><ul><li>Rectangle</li><li>Kidney</li><li>Classic</li><li>Freeform</li><li>Lap Pools</li></ul></div>
  <div class="option-col col-styles"><h3>Styles</h3><ul><li>Seabreeze</li><li>Harbor Cove</li><li>Sandpiper</li><li>Driftwood</li><li>Marlowe</li></ul></div>
  <div class="option-col col-colors"><h3>Colors</h3><ul><li>Ocean Blue</li><li>Pearl White</li><li>Slate Grey</li><li>Desert Sand (brown)</li><li>Lagoon Blue</li></ul></div>
</div>

<div class="abs feature-photo" role="img" aria-label="Woman in a sun hat relaxing at the edge of an infinity pool"></div>
<div class="abs slide-arrow" style="left:448px">
  <svg width="6" height="10" viewBox="0 0 6 10"><path d="M5 1 1 5l4 4" fill="none" stroke="#7a8a9a" stroke-width="1.4"/></svg>
</div>
<div class="abs slide-arrow" style="left:644px">
  <svg width="6" height="10" viewBox="0 0 6 10"><path d="M1 1l4 4-4 4" fill="none" stroke="#7a8a9a" stroke-width="1.4"/></svg>
</div>

<div class="abs rule" style="top:601px"></div>

<h2 class="abs section-title portfolio-title"><span class="accent">LATEST</span> PORTFOLIO</h2>
<p class="abs body-text portfolio-text">Our portfolio is very extensive. What is shown here online is merely a portion of what we have done in the valley. Feel free to check out some of our work, they are broken up into four categories; pools, spools and spas, beehives, and water features.</p>

<div class="abs tile tile-feature" style="left:66px;top:682px">
  <h4>FIBERGLASS POOLS</h4>
  <p>We built our business on making quality Fiberglass pools. With many sizes and style to choose from, it is easy to see why browsing through our pools.</p>
  <div class="tile-icons">
    <svg width="9" height="9" viewBox="0 0 10 10"><path d="M1 4v5h7V6" fill="none" stroke="#fff" stroke-width="1"/><path d="M4 6 9 1M6 1h3v3" fill="none" stroke="#fff" stroke-width="1"/></svg>
    <svg width="9" height="9" viewBox="0 0 10 10"><circle cx="4" cy="4" r="3" fill="none" stroke="#fff" stroke-width="1.2"/><line x1="6.2" y1="6.2" x2="9" y2="9" stroke="#fff" stroke-width="1.3"/></svg>
  </div>
</div>
<div class="abs tile p1" style="left:217px;top:682px" role="img" aria-label="Curved backyard pool with palm trees"></div>
<div class="abs tile p2" style="left:367px;top:682px" role="img" aria-label="Pool at night with rock waterfall"></div>
<div class="abs tile p3" style="left:517px;top:682px" role="img" aria-label="Small spa pool beside a house"></div>
<div class="abs tile p4" style="left:66px;top:794px" role="img" aria-label="Rectangular pool with wooden deck and palms"></div>
<div class="abs tile p5" style="left:217px;top:794px" role="img" aria-label="Resort pool with umbrellas and loungers"></div>
<div class="abs tile p6" style="left:367px;top:794px" role="img" aria-label="Woman in a sun hat at an infinity pool"></div>
<div class="abs tile p7" style="left:517px;top:794px" role="img" aria-label="Seaside pool with stepping stones and umbrella"></div>

<div class="abs rule" style="top:920px"></div>

<h2 class="abs section-title about-title"><span class="accent">ABOUT</span> US</h2>
<p class="abs body-text about-text">Tidemoor Pools was founded for one simple reason, to make a better pools. We are family owned and operated, and Tidemoor Pools has been serving the valley for years. Chances are if you you are in AZ and you step into a pool that feels extraordinarily smooth, Tidemoor Pools was responsible for it. The difference is fiberglass. Fiberglass pools Years of building pools made from the finest fiberglass pool shells has made us an expert in more than just pool building. We can build spools, spas, beehives, water features, are smoother, they have lower maintenance costs, they are easier to keep clean, and they retain water better.</p>

<div class="abs cta">Click Here For More Info</div>

<div class="abs social"><span></span><span></span><span></span><span></span></div>

<div class="abs footer-nav">Home<span class="sep">/</span>Style<span class="sep">/</span>Portfolio<span class="sep">/</span>Installation<span class="sep">/</span>About Us<span class="sep">/</span>Contact Us</div>
<div class="abs copyright">© Copy Rights 2015 Tidemoor Pools.All Rights Reserver.</div>

</body>
</html>
```